I am looking for a whole Stationery Design for my Company. A new Logo, Letterhead and Business Card. I have attached an old Logo which looks very bad. Be creative and use your own ideas for the Logo as well as all other designs.

```html
<!DOCTYPE html>
<html lang="en">
<head>
<meta charset="utf-8">
<title>Tsheleng Projects – Stationery</title>
<link rel="stylesheet" href="https://fonts.googleapis.com/css2?family=Montserrat:wght@400;500;600;700&display=swap">
<style>
  :root{
    --orange:#d4641c;
    --orange-light:#e67a1c;
    --orange-deep:#8e3a17;
    --brown:#5b2a22;
    --text:#4a4a4a;
    --pink:#e8175d;
    --amber:#f7941d;
    --slate:#6b6b6b;
    --teal:#4aa3b5;
    --ink:#333333;
    --fb:#3b5998;
    --sky:#55acee;
    --rose:#d6486b;
  }
  *{margin:0;padding:0;box-sizing:border-box}
  html,body{width:849px;height:1200px;overflow:hidden;background:#fff}
  body{font-family:"Montserrat",sans-serif;color:var(--text)}
  .sheet{position:relative;width:849px;height:1200px;overflow:hidden;background:#fff}

  .header-band{position:absolute;left:0;top:0;width:849px;height:215px;
    background:linear-gradient(100deg,#cf6a1c 0%,#d4641c 45%,#b24e1a 80%,#8a3416 100%)}

  .brand{position:absolute;display:flex;align-items:flex-start;gap:10px;font-family:"Montserrat",sans-serif;font-weight:600;color:var(--brown);line-height:1}
  .brand-mark{background:var(--brown);flex:none}
  .brand-name span{display:block}
  .brand-name .sub{margin-left:1px}

  .brand--header{left:40px;top:104px}
  .brand--header .brand-mark{width:34px;height:34px;margin-top:4px}
  .brand--header .brand-name{font-size:40px;letter-spacing:-.5px}
  .brand--header .brand-name .sub{font-size:21px;letter-spacing:7px;margin-top:6px}

  .card{position:absolute;left:226px;width:380px;height:235px;overflow:hidden}
  .card--front{top:413px;background:linear-gradient(135deg,var(--orange-light) 0%,var(--orange) 50%,var(--orange-deep) 100%)}
  .card--front .brand{left:117px;top:115px}
  .card--front .brand-mark{width:22px;height:22px;margin-top:4px}
  .card--front .brand-name{font-size:26px;letter-spacing:-.3px}
  .card--front .brand-name .sub{font-size:16px;letter-spacing:5px;margin-top:5px}
  .card-url{position:absolute;left:0;right:0;top:209px;text-align:center;color:#fff;font-size:7.5px;letter-spacing:3.2px}
  .card-url b{font-weight:700}

  .card--back{top:661px;background:linear-gradient(120deg,#e4e4e4 0%,#f7f7f7 45%,#eeeeee 70%,#d6d6d6 100%)}
  .card--back .brand{left:47px;top:115px}
  .card--back .brand-mark{width:17px;height:17px;margin-top:2px}
  .card--back .brand-name{font-size:19px;letter-spacing:-.2px}
  .card--back .brand-name .sub{font-size:12px;letter-spacing:3.5px;margin-top:4px}
  .card-divider{position:absolute;left:189px;top:20px;width:1px;height:195px;background:#cfcfcf}
  .card-person{position:absolute;left:205px;top:46px;font-size:10.5px;color:var(--slate)}
  .card-person b{color:var(--brown);font-weight:600}
  .card-rule{position:absolute;top:64px;height:1.5px}
  .card-rule--dark{left:205px;width:119px;background:var(--slate)}
  .card-rule--accent{left:326px;width:34px;background:var(--orange)}
  .card-contact{position:absolute;left:205px;list-style:none;font-size:8.5px;color:var(--text)}
  .card-contact li{display:flex;align-items:center;gap:7px;height:11px}
  .card-contact b{font-weight:600}

  .icon{display:inline-flex;align-items:center;justify-content:center;flex:none}
  .icon svg{display:block}
  .icon-sm{width:8px;height:8px}
  .icon-md{width:13px;height:13px}
  .i-home{background:var(--pink)}
  .i-phone{background:var(--amber)}
  .i-fax{background:var(--slate)}
  .i-mail{background:var(--teal)}
  .i-web{background:var(--ink)}
  .i-fb{background:var(--fb)}
  .i-tw{background:var(--sky)}
  .i-ig{background:var(--rose)}

  .footer-contact{position:absolute;list-style:none;font-size:13px;color:var(--text);letter-spacing:.3px}
  .footer-contact li{display:flex;align-items:center;gap:10px;height:18px}
  .footer-contact b{font-weight:600}
  .footer-contact--left{left:31px;top:1104px}
  .footer-contact--mid{left:296px;top:1124px}
  .footer-social{position:absolute;left:723px;top:1128px;display:flex;gap:9px}
  .footer-social span{width:25px;height:25px;display:block}
  .footer-band{position:absolute;left:0;top:1158px;width:849px;height:42px;background:linear-gradient(100deg,#dcdcdc 0%,#f4f4f4 40%,#ececec 70%,#cfcfcf 100%)}
</style>
</head>
<body>
<main class="sheet">

  <div class="header-band" role="img" aria-label="Decorative orange and brown wave header"></div>

  <div class="brand brand--header">
    <span class="brand-mark"></span>
    <div class="brand-name"><span>Tsheleng</span><span class="sub">Projects</span></div>
  </div>

  <section class="card card--front">
    <div class="brand">
      <span class="brand-mark"></span>
      <div class="brand-name"><span>Tsheleng</span><span class="sub">Projects</span></div>
    </div>
    <p class="card-url">www.<b>tshelengprojects</b>.com</p>
  </section>

  <section class="card card--back">
    <div class="brand">
      <span class="brand-mark"></span>
      <div class="brand-name"><span>Tsheleng</span><span class="sub">Projects</span></div>
    </div>
    <span class="card-divider"></span>
    <p class="card-person"><b>Lerato Dube</b>, Designation</p>
    <span class="card-rule card-rule--dark"></span>
    <span class="card-rule card-rule--accent"></span>
    <ul class="card-contact" style="top:81px">
      <li><span class="icon icon-sm i-home"></span>58 Marula Rd. Polokwane, LP 0699</li>
    </ul>
    <ul class="card-contact" style="top:97px">
      <li><span class="icon icon-sm i-phone"></span>015 240 7713</li>
      <li><span class="icon icon-sm i-fax"></span>015 240 7713</li>
    </ul>
    <ul class="card-contact" style="top:125px">
      <li><span class="icon icon-sm i-mail"></span><span><b>info</b>@tshelengprojects.com</span></li>
      <li><span class="icon icon-sm i-web"></span><span>www.<b>tshelengprojects</b>.com</span></li>
    </ul>
    <ul class="card-contact" style="top:153px">
      <li><span class="icon icon-sm i-fb"></span>tshelengprojects</li>
      <li><span class="icon icon-sm i-tw"></span>#tshelengprojects</li>
      <li style="margin-top:2px"><span class="icon icon-sm i-ig"></span>tshelengprojects</li>
    </ul>
  </section>

  <ul class="footer-contact footer-contact--left">
    <li><span class="icon icon-md i-home"><svg width="9" height="9" viewBox="0 0 10 10"><path d="M1 5 L5 1.5 L9 5 V9 H6 V6.5 H4 V9 H1 Z" fill="#fff"/></svg></span>58 Marula Rd. Polokwane, LP 0699</li>
    <li style="margin-top:2px"><span class="icon icon-md i-phone"><svg width="9" height="9" viewBox="0 0 10 10"><path d="M2.5 1 L4 3 L3 4 C3.6 5.3 4.7 6.4 6 7 L7 6 L9 7.5 L8 9 C4.5 8.8 1.2 5.5 1 2 Z" fill="#fff"/></svg></span>015 240 7713</li>
    <li><span class="icon icon-md i-fax"><svg width="9" height="9" viewBox="0 0 10 10"><rect x="3" y="1" width="4" height="3" fill="#fff"/><rect x="1" y="4" width="8" height="3.5" fill="#fff"/><rect x="3" y="6.5" width="4" height="2.5" fill="#fff"/></svg></span>015 240 7713</li>
  </ul>

  <ul class="footer-contact footer-contact--mid">
    <li><span class="icon icon-md i-mail"><svg width="9" height="9" viewBox="0 0 10 10"><rect x="1" y="2.5" width="8" height="5.5" fill="none" stroke="#fff" stroke-width="1"/><path d="M1 2.5 L5 6 L9 2.5" fill="none" stroke="#fff" stroke-width="1"/></svg></span><span><b>info</b>@tshelengprojects.com</span></li>
    <li><span class="icon icon-md i-web"><svg width="9" height="9" viewBox="0 0 10 10"><circle cx="5" cy="5" r="3.8" fill="none" stroke="#fff" stroke-width="0.9"/><path d="M1.2 5 H8.8 M5 1.2 V8.8" stroke="#fff" stroke-width="0.8"/></svg></span><span>www.<b>tshelengprojects</b>.com</span></li>
  </ul>

  <div class="footer-social" aria-label="Social profiles">
    <span class="i-fb"></span>
    <span class="i-tw"></span>
    <span class="i-ig"></span>
  </div>

  <div class="footer-band" aria-hidden="true"></div>
</main>
</body>
</html>
```